E Liquid Label design R

Im starting by seying that i dont speak or write Inglés, i dont speak spanish since i am from Paraguay, im very sorry for That, try my best to get Understood. I am startin a company of e liquids, (electronic cigarrettes). the liquid production is ok but the label is not. i try to do my label here with a graphic designer (friend of mine) but is is very busy esta days and I HAD no time for esta. but have made me one label, that i will atach here, That is nice, but is not that i want, because i tell him the name will be "corvex" (the first alchemist in the world) i tell him that i wanted to explore themes like magic, vapors, etc. mistery but looking now is kind of boring. I really like something more hip and modern with a design work, What i do know is that i want to put a red wax seal on the top center of the glass bottle (will attach pics) i really really like the tinbrook artwork, simple, hip, modern, fix in your mind. will attach pics for Those Who dont know the brand, also like the i want to design for 30 ml bottles made of clear glass with dropper (childproof) approx 40 x 90 milimeters in size. i am starting with 8 flavors, so, the design has to be adaptable for each flavor. It has to say somewere the strength level of nicotine 0 -3-6 - 9 to 12 mg in a creative way, maybe some stairs With the levels and the level it has to say Highlighted somewere USA made with ingredients, with some flag or something in the small font section will be warnings, ingredients and other stuff that i will update tomorrow.

Target Market(s)

quitting smokers, vapers

Requirements
Must have
• network (or maybe other color) wax seal as described in the description i wiil update in soon esta sección
Nice to have

```html
<!DOCTYPE html>
<html lang="en">
<head>
<meta charset="utf-8">
<title>Corvex E-Liquid Labels</title>
<link rel="stylesheet" href="https://fonts.googleapis.com/css2?family=Pathway+Gothic+One&family=Cinzel:wght@700&display=swap">
<style>
  :root {
    --canvas: #ffffff;
    --ink: #0a0a0a;
    --paper: #ffffff;
    --fire-main: #f26522;
    --fire-light: #f7941d;
    --fire-deep: #ed1c24;
    --mist-main: #8b3a96;
    --mist-light: #a24fae;
    --mist-deep: #3a1a4a;
    --flag-red: #c8102e;
    --flag-blue: #3c3b6e;
  }
  * { box-sizing: border-box; margin: 0; padding: 0; }
  html, body { width: 1200px; height: 1000px; overflow: hidden; background: var(--canvas); }
  body { position: relative; font-family: "Pathway Gothic One", "Arial Narrow", sans-serif; }

  .label {
    position: absolute; top: 47px; width: 465px; height: 930px;
    background: var(--ink); overflow: hidden; color: var(--paper);
  }
  .label--emberline { left: 92px; --main: var(--fire-main); --light: var(--fire-light); --deep: var(--fire-deep); }
  .label--violet-haze { left: 634px; --main: var(--mist-main); --light: var(--mist-light); --deep: var(--mist-deep); }

  .label__wave { position: absolute; left: 0; top: 0; width: 465px; height: 260px; }

  .ingredients {
    position: absolute; left: 14px; top: 24px; width: 445px;
    font-size: 17px; line-height: 24px; color: var(--paper);
  }
  .nicotine {
    position: absolute; left: 63px; top: 93px; display: flex; align-items: center;
    font-size: 17px;
  }
  .nicotine__caption { margin-right: 10px; }
  .nicotine__level {
    width: 26px; height: 24px; margin-right: 13px; background: var(--paper); color: var(--ink);
    display: flex; align-items: center; justify-content: center; font-size: 16px;
  }

  .flavor-band {
    position: absolute; left: 48px; top: 330px; width: 60px; height: 240px;
    background: linear-gradient(180deg, var(--light), var(--main));
    transform: rotate(-4deg);
  }
  .flavor-band__name {
    position: absolute; left: 50%; top: 50%;
    transform: translate(-50%, -50%) rotate(90deg);
    font-family: "Cinzel", Georgia, serif; font-weight: 700; font-size: 17px;
    letter-spacing: 1px; white-space: nowrap; color: var(--paper);
  }

  .brand-name { position: absolute; left: 170px; top: 455px; width: 0; height: 0; }
  .brand-name__text {
    position: absolute; transform: translate(-50%, -50%) rotate(90deg);
    font-size: 72px; letter-spacing: 8px; color: var(--paper); white-space: nowrap;
  }
  .brand-ring {
    position: absolute; left: 225px; top: 372px; width: 150px; height: 150px;
    border: 11px solid var(--main); border-radius: 50%;
  }

  .origin { position: absolute; left: 15px; top: 670px; display: flex; align-items: flex-start; }
  .origin__flag {
    width: 37px; height: 73px; position: relative;
    background: repeating-linear-gradient(90deg, var(--flag-red) 0 4px, var(--paper) 4px 8px);
  }
  .origin__flag::before {
    content: ""; position: absolute; right: 0; top: 0; width: 18px; height: 34px; background: var(--flag-blue);
  }
  .origin__text {
    writing-mode: vertical-rl; font-size: 12px; line-height: 12px; margin-left: 3px;
    text-transform: uppercase; white-space: nowrap;
  }

  .warning {
    position: absolute; left: 12px; width: 444px;
    font-size: 12.5px; line-height: 15.8px; text-align: justify; hyphens: auto;
  }
  .warning--en { top: 752px; }
  .warning--es { top: 834px; }
</style>
</head>
<body>

<section class="label label--emberline" aria-label="Emberline flavor label">
  <svg class="label__wave" viewBox="0 0 465 260" aria-hidden="true">
    <defs>
      <linearGradient id="fire-wave" x1="0" x2="1">
        <stop offset="0" stop-color="#f26522"/><stop offset="1" stop-color="#f7941d"/>
      </linearGradient>
    </defs>
    <rect width="465" height="200" fill="var(--fire-main)"/>
    <path d="M0,165 C130,120 260,190 465,130 L465,260 L0,260Z" fill="url(#fire-wave)"/>
    <path d="M0,205 C140,165 270,230 465,178 L465,260 L0,260Z" fill="var(--fire-deep)"/>
    <path d="M0,235 C150,200 280,250 465,200 L465,260 L0,260Z" fill="var(--ink)"/>
  </svg>
  <p class="ingredients">INGREDIENTS: USP Vegetable Glycerin, USP Propylene Glycol, Natural and Artificial food Flavorings.</p>
  <div class="nicotine">
    <span class="nicotine__caption">Nicotine Level: mg/mL</span>
    <span class="nicotine__level">0</span><span class="nicotine__level">3</span><span class="nicotine__level">6</span><span class="nicotine__level">9</span><span class="nicotine__level">12</span>
  </div>
  <div class="flavor-band"><span class="flavor-band__name">EMBERLINE</span></div>
  <div class="brand-name"><span class="brand-name__text">CORVEX</span></div>
  <div class="brand-ring"></div>
  <div class="origin">
    <div class="origin__flag" role="img" aria-label="United States flag"></div>
    <span class="origin__text">Made in the USA</span>
  </div>
  <p class="warning warning--en">Warning: Our products may contain nicotine, wich is highly addictive. Not for sale to minors. Product not recommended for pregnant women and people with cardiovascular problems. Lock up an keep out of the reach of children and pets. In case of CONTACT TO SKIN: Wash thoroughly with soap and water. If you feel unwell consult a doctor ASAP, and keep product container or label with you.</p>
  <p class="warning warning--es" lang="es">ATENCION: Nuestros productos podrian o no contener nicotina, la cual es altamente adictiva. NO debe venderse a menores. Producto no recomendado para mujeres embarazadas y personas con problemas cardiovasculares. Mantener bajo llave y lejos del alcance de niños y mascotas. En caso de CONTACO CON LA PIEL: lavar con abundante agua y jabon. Si usando este producto se siente mareado y/o con otras molestias, consulte con un Doctor inmediatamente, llevando consigo el envase o la etiqueta de este producto.</p>
</section>

<section class="label label--violet-haze" aria-label="Violet Haze flavor label">
  <svg class="label__wave" viewBox="0 0 465 260" aria-hidden="true">
    <rect width="465" height="200" fill="var(--mist-main)"/>
    <path d="M0,165 C130,120 260,190 465,130 L465,260 L0,260Z" fill="var(--mist-light)"/>
    <path d="M0,195 C140,155 270,220 465,168 L465,260 L0,260Z" fill="var(--mist-deep)"/>
    <path d="M0,235 C150,200 280,250 465,200 L465,260 L0,260Z" fill="var(--ink)"/>
  </svg>
  <p class="ingredients">INGREDIENTS: USP Vegetable Glycerin, USP Propylene Glycol, Natural and Artificial food Flavorings.</p>
  <div class="nicotine">
    <span class="nicotine__caption">Nicotine Level: mg/mL</span>
    <span class="nicotine__level">0</span><span class="nicotine__level">3</span><span class="nicotine__level">6</span><span class="nicotine__level">9</span><span class="nicotine__level">12</span>
  </div>
  <div class="flavor-band"><span class="flavor-band__name">VIOLET HAZE</span></div>
  <div class="brand-name"><span class="brand-name__text">CORVEX</span></div>
  <div class="brand-ring"></div>
  <div class="origin">
    <div class="origin__flag" role="img" aria-label="United States flag"></div>
    <span class="origin__text">Made in the USA</span>
  </div>
  <p class="warning warning--en">Warning: Our products may contain nicotine, wich is highly addictive. Not for sale to minors. Product not recommended for pregnant women and people with cardiovascular problems. Lock up an keep out of the reach of children and pets. In case of CONTACT TO SKIN: Wash thoroughly with soap and water. If you feel unwell consult a doctor ASAP, and keep product container or label with you.</p>
  <p class="warning warning--es" lang="es">ATENCION: Nuestros productos podrian o no contener nicotina, la cual es altamente adictiva. NO debe venderse a menores. Producto no recomendado para mujeres embarazadas y personas con problemas cardiovasculares. Mantener bajo llave y lejos del alcance de niños y mascotas. En caso de CONTACO CON LA PIEL: lavar con abundante agua y jabon. Si usando este producto se siente mareado y/o con otras molestias, consulte con un Doctor inmediatamente, llevando consigo el envase o la etiqueta de este producto.</p>
</section>

</body>
</html>
```